Business card design needed

I am a free lance management consultant looking to have some professionally designed business cards created.
If possible if i could have some bullet points or something with a list of my services that would be great.
Services are:
- Strategic Planning
- Process Improvement
- Change Management
- IT Solutions & Implementation
- IT Consulting
- Web Solutions
Target Market(s)
Business Owners and Operators
Industry/Entity Type
Business
Contact Information for Business Card
Peter Whitlock
PW Consulting
0438 516 274
PETER@PETERWHITLOCK.EXAMPLE
www.peterwhitlock.example
Logo Text
PW Consulting
Logo styles of interest
Pictorial/Combination Logo
Wordmark Logo
Lettermark Logo
Look and feel
Each slider illustrates characteristics of the customer's brand and the style your logo design should communicate.

```html
<!DOCTYPE html>
<html lang="en">
<head>
<meta charset="utf-8">
<title>PW Consulting – Business Card</title>
<link rel="stylesheet" href="https://fonts.googleapis.com/css2?family=Archivo:wght@700&family=Roboto+Condensed:wght@700&display=swap">
<style>
  :root {
    --backdrop: #ebeceb;
    --card: #ffffff;
    --ink: #111111;
    --charcoal: #2c2a28;
    --accent: #ff0000;
  }
  * { margin: 0; padding: 0; box-sizing: border-box; }
  html, body { width: 1200px; height: 491px; overflow: hidden; }
  body { background: var(--backdrop); position: relative; font-family: "Archivo", Arial, sans-serif; color: var(--ink); }

  .card {
    position: absolute;
    width: 552px;
    height: 320px;
    background: var(--card);
    box-shadow: 4px 5px 10px rgba(0,0,0,0.35);
    overflow: hidden;
  }
  .card--front { left: 36px; top: 76px; height: 319px; }
  .card--back { left: 621px; top: 76px; }
  .card__art { position: absolute; inset: 0; }

  .holder-name {
    position: absolute; left: 48px; top: 88px;
    font-size: 22px; letter-spacing: 0.6px;
  }
  .contact {
    position: absolute; left: 48px;
    font-family: "Roboto Condensed", "Arial Narrow", sans-serif;
    font-size: 16px; line-height: 1;
  }
  .contact--mobile { top: 152px; }
  .contact--email { top: 177px; }
  .contact--web { top: 231px; font-family: "Archivo", Arial, sans-serif; font-size: 16px; letter-spacing: 0.4px; }

  .brand {
    position: absolute; width: 220px; margin-left: -110px;
    text-align: center; color: var(--accent);
    font-family: "Roboto Condensed", "Arial Narrow", sans-serif;
    line-height: 1;
  }
  .card--front .brand { left: 449px; top: 174px; }
  .card--back .brand { left: 111px; top: 174px; }
  .brand__initials { display: block; font-size: 28px; letter-spacing: 1px; }
  .brand__word { display: block; font-size: 24px; margin-top: 6px; }

  .phone-line {
    position: absolute; left: 38px; top: 249px;
    display: flex; align-items: center; gap: 8px;
    color: var(--accent);
    font-family: "Roboto Condensed", "Arial Narrow", sans-serif;
    font-size: 20px;
  }
  .phone-line svg { width: 16px; height: 18px; }

  .services {
    position: absolute; left: 236px; top: 97px;
    list-style: none;
    font-size: 16px; letter-spacing: 0.5px; line-height: 28px;
  }
  .services li { position: relative; padding-left: 18px; }
  .services li::before {
    content: ""; position: absolute; left: 2px; top: 12px;
    width: 6px; height: 6px; border-radius: 50%; background: var(--accent);
  }
</style>
</head>
<body>

<section class="card card--front">
  <svg class="card__art" viewBox="0 0 552 319" aria-hidden="true">
    <defs>
      <linearGradient id="fade-front" x1="0" y1="0" x2="0" y2="1">
        <stop offset="0" stop-color="#2c2a28"/>
        <stop offset="0.15" stop-color="#3b3937"/>
        <stop offset="1" stop-color="#ffffff"/>
      </linearGradient>
    </defs>
    <rect x="346" y="69" width="206" height="187" fill="url(#fade-front)"/>
    <polygon points="304,0 552,0 552,70 346,70" fill="var(--charcoal)"/>
    <polygon points="304,1 346,70 304,70" fill="var(--accent)"/>
  </svg>

  <h1 class="holder-name">Peter Whitlock</h1>
  <p class="contact contact--mobile">Mobile: 0438 516 274</p>
  <p class="contact contact--email">E-mail: PETER@PETERWHITLOCK.EXAMPLE</p>
  <p class="contact contact--web">www.peterwhitlock.example</p>

  <p class="brand"><span class="brand__initials">PW</span><span class="brand__word">Consulting</span></p>
</section>

<section class="card card--back">
  <svg class="card__art" viewBox="0 0 552 320" aria-hidden="true">
    <defs>
      <linearGradient id="fade-back" x1="0" y1="0" x2="0" y2="1">
        <stop offset="0" stop-color="#2c2a28"/>
        <stop offset="0.15" stop-color="#3b3937"/>
        <stop offset="1" stop-color="#ffffff"/>
      </linearGradient>
    </defs>
    <rect x="0" y="69" width="206" height="187" fill="url(#fade-back)"/>
    <polygon points="0,0 247,0 206,70 0,70" fill="var(--charcoal)"/>
    <polygon points="247,1 247,70 206,70" fill="var(--accent)"/>
  </svg>

  <p class="brand"><span class="brand__initials">PW</span><span class="brand__word">Consulting</span></p>

  <p class="phone-line">
    <svg viewBox="0 0 16 18" aria-hidden="true">
      <path d="M4 1 L6.5 4.5 L5 6.5 C5.8 9 7.2 11 9.3 12.6 L11.2 11.2 L14.5 13.8 L12.8 16.6 C7.5 16 2.4 9.5 1.6 3.2 Z" fill="none" stroke="var(--accent)" stroke-width="1.6" stroke-linejoin="round"/>
    </svg>
    <span>0438 516 274</span>
  </p>

  <ul class="services">
    <li>Strategic Planning</li>
    <li>Process Improvement</li>
    <li>Change Management</li>
    <li>IT Solutions &amp; Implementation</li>
    <li>IT Consulting</li>
    <li>Web Solutions</li>
  </ul>
</section>

</body>
</html>
```